Business card for law firm

Need business card for new law firm. Think confident, authoritative, conservative, but not stuffy or old-fashioned.

Contact Information for Business Card

Content for card - logo (uploaded), plus the following:

Paul Weybridge (larger font)
Managing Partner (larger font, but not as large as name)
Level 9, 47 Calder Lane
Sydney NSW 2000
Main Tel 02 7304 6219
Direct Tel 02 7462 3158
Email paul@wbrlegal.com.au
www.wbrlegal.com.au

Letterhead design should include logo plus:
Level 9, 47 Calder Lane
Sydney NSW 2000
Tel 02 7462 3158
www.wbrlegal.com.au

```html
<!DOCTYPE html>
<html lang="en">
<head>
<meta charset="utf-8">
<title>Weybridge Lawyers — Business Card</title>
<link href="https://fonts.googleapis.com/css2?family=Noto+Serif:wght@400;700&display=swap" rel="stylesheet">
<style>
  :root {
    --navy: #1f2452;
    --ink: #222326;
    --paper: #ffffff;
    --backdrop: #e9eaec;
  }
  * { box-sizing: border-box; margin: 0; padding: 0; }
  html, body { width: 1154px; height: 1200px; overflow: hidden; }
  body {
    background: var(--backdrop);
    font-family: "Noto Serif", Georgia, serif;
    position: relative;
  }
  .card {
    position: absolute;
    width: 900px;
    height: 540px;
    border-radius: 26px;
    box-shadow: 0 6px 14px rgba(0,0,0,0.18);
  }

  /* Front */
  .card-front {
    left: 70px; top: 40px;
    background: var(--navy);
    color: var(--paper);
  }
  .front-mark {
    position: absolute; left: 390px; top: 78px;
    width: 120px; height: 120px;
    background: var(--paper);
  }
  .front-name {
    position: absolute; left: 0; right: 0; top: 250px;
    text-align: center;
    font-size: 76px; font-weight: 400; letter-spacing: 0.02em;
    line-height: 1;
  }
  .front-sub {
    position: absolute; left: 0; right: 0; top: 350px;
    text-align: center;
    font-size: 32px; font-weight: 400; letter-spacing: 0.9em;
    padding-left: 0.9em; line-height: 1;
  }
  .front-web {
    position: absolute; left: 0; right: 0; top: 470px;
    text-align: center; font-size: 27px; line-height: 1;
  }

  /* Back */
  .card-back {
    left: 184px; top: 630px;
    background: var(--paper);
    color: var(--ink);
  }
  .back-brand {
    position: absolute; left: 40px; top: 170px; width: 380px;
    text-align: center; color: var(--ink);
  }
  .back-mark {
    width: 70px; height: 70px; background: var(--navy);
    margin: 0 auto 22px;
  }
  .back-name { font-size: 44px; font-weight: 400; line-height: 1; letter-spacing: 0.02em; }
  .back-sub { font-size: 19px; letter-spacing: 0.9em; padding-left: 0.9em; margin-top: 8px; line-height: 1; }
  .divider {
    position: absolute; left: 450px; top: 110px;
    width: 3px; height: 330px; background: var(--navy);
  }
  .details { position: absolute; left: 475px; top: 125px; right: 20px; }
  .person { font-size: 37px; font-weight: 700; color: var(--navy); line-height: 1.05; }
  .role { font-size: 28px; margin-top: 6px; line-height: 1.1; }
  .row { display: flex; align-items: flex-start; margin-top: 24px; }
  .row svg { width: 28px; height: 28px; flex: none; margin-right: 20px; margin-top: 4px; fill: var(--navy); }
  .row p { font-size: 25px; line-height: 1.3; }
  .note { font-size: 15px; }
</style>
</head>
<body>
  <section class="card card-front">
    <div class="front-mark"></div>
    <div class="front-name">WEYBRIDGE</div>
    <div class="front-sub">LAWYERS</div>
    <div class="front-web">www.wbrlegal.com.au</div>
  </section>

  <section class="card card-back">
    <div class="back-brand">
      <div class="back-mark"></div>
      <div class="back-name">WEYBRIDGE</div>
      <div class="back-sub">LAWYERS</div>
    </div>
    <div class="divider"></div>
    <div class="details">
      <h1 class="person">PAUL WEYBRIDGE</h1>
      <h2 class="role" style="font-weight:400">MANAGING PARTNER</h2>
      <div class="row">
        <svg viewBox="0 0 24 24" aria-hidden="true"><path d="M12 2a7 7 0 0 0-7 7c0 5 7 13 7 13s7-8 7-13a7 7 0 0 0-7-7zm0 9.5A2.5 2.5 0 1 1 12 6.5a2.5 2.5 0 0 1 0 5z"/></svg>
        <p>Level 9, 47 Calder Lane<br>Sydney | NSW | 2000</p>
      </div>
      <div class="row">
        <svg viewBox="0 0 24 24" aria-hidden="true"><path d="M6.6 10.8a15 15 0 0 0 6.6 6.6l2.2-2.2a1 1 0 0 1 1-.25 11.4 11.4 0 0 0 3.6.57 1 1 0 0 1 1 1V20a1 1 0 0 1-1 1A17 17 0 0 1 3 4a1 1 0 0 1 1-1h3.5a1 1 0 0 1 1 1c0 1.25.2 2.45.57 3.57a1 1 0 0 1-.25 1z"/></svg>
        <p>02 7304 6219 <span class="note">(main)</span><br>02 7462 3158 <span class="note">(direct)</span></p>
      </div>
      <div class="row">
        <svg viewBox="0 0 24 24" aria-hidden="true"><path d="M2 5h20v14H2zm2 2v.4l8 5.6 8-5.6V7zm0 2.8V17h16V9.8l-8 5.6z"/></svg>
        <p>paul@wbrlegal.com.au</p>
      </div>
    </div>
  </section>
</body>
</html>
```